Federal Government Proposal Development Consulting company needs a website designed and coded

I am looking for someone to design (using an existing logo, color palette, and text fonts) and code a wordpress-based website for a Proposal Development consulting company. I have full copy for all site pages and suggestions for images/ graphics and a few example design templates to go from.

One note, from a color perspective - I included a mockup of a business card to highlight a color scheme that I tend to like - if you look at the back of the business card, the blend of the grey, blue, with the neon green highlight as a separator really seems to pop. Just a thought as you are designing the page.

I would like to see 2-3 potential design layouts, and I will select one to move forward with. Then, I would like the site to be coded for WordPress (I can provide a login to my wordpress site). I would like 1 opportunity to review the coded site and make any final tweaks.

```html
<!DOCTYPE html>
<html lang="en">
<head>
<meta charset="utf-8">
<title>Calder Bid Partners</title>
<link rel="stylesheet" href="https://fonts.googleapis.com/css2?family=Gentium+Book+Plus:ital,wght@0,400;1,400&family=Montserrat:wght@400;500;600;700&family=Raleway:wght@400;500&display=swap">
<style>
:root{
  --navy:#120d62;
  --teal:#1ff0b8;
  --ink:#222;
  --muted:#7a7a8a;
  --footer:#333333;
  --footer-text:#a9a9a9;
  --white:#fff;
  --serif:'Gentium Book Plus', Georgia, serif;
  --sans:'Montserrat', Arial, sans-serif;
  --light:'Raleway', Arial, sans-serif;
}
*{box-sizing:border-box;margin:0;padding:0}
html,body{width:1200px;height:3424px;overflow:hidden;background:#fff}
body{position:relative;font-family:var(--sans);color:var(--ink)}

/* header */
.site-header{position:absolute;left:0;top:0;width:1200px;height:76px;background:#fff;border-top:3px solid var(--teal)}
.brand{position:absolute;left:190px;top:24px;display:flex;align-items:center;gap:10px}
.brand-name{font-family:var(--sans);font-weight:600;font-size:19px;color:var(--navy);line-height:1;white-space:nowrap}
.brand-dot{width:22px;height:22px;border-radius:50%;background:var(--navy)}
.social{position:absolute;left:934px;top:8px;display:flex;gap:5px}
.social span{width:10px;height:10px;border-radius:50%;background:var(--navy)}
.main-nav{position:absolute;top:36px;left:568px;display:flex;gap:39px;font-family:var(--light);font-size:13px;color:#333}
.main-nav a{color:#333;text-decoration:none;padding-bottom:6px}
.main-nav a.active{border-bottom:3px solid var(--navy)}

/* hero */
.hero{position:absolute;left:0;top:76px;width:1200px;height:379px;overflow:hidden}
.hero-photo{position:absolute;inset:0;background:linear-gradient(100deg,#5a4a3f 0%,#8d7360 25%,#b9a38f 45%,#6e6158 70%,#3b3a45 100%)}
.hero-disc{position:absolute;left:580px;top:-94px;width:474px;height:474px;border-radius:50%;background:var(--navy)}
.hero-title{position:absolute;left:687px;top:48px;font-family:var(--serif);font-weight:400;font-size:72px;line-height:62px;color:#fff}
.hero-sub{position:absolute;left:687px;top:186px;font-family:var(--light);font-size:18px;line-height:21px;color:#fff;white-space:nowrap}
.hero-btn{position:absolute;left:688px;top:244px;width:190px;height:33px;background:var(--teal);color:var(--navy);font-size:9px;font-weight:700;white-space:nowrap;display:flex;align-items:center;justify-content:center;gap:8px}
.hero-dots{position:absolute;left:550px;top:340px;display:flex;gap:18px}
.hero-dots span{width:22px;height:3px;background:rgba(255,255,255,.35)}
.hero-dots span.on{background:#fff}
.hero-shadow{position:absolute;left:70px;top:455px;width:1060px;height:28px;background:radial-gradient(ellipse at top,rgba(0,0,0,.28),rgba(0,0,0,0) 70%)}

/* section headings */
.section-title{position:absolute;font-family:var(--serif);font-weight:400;color:var(--navy);font-size:38px;line-height:1}

/* what we do */
.what-col{position:absolute;width:333px;font-family:var(--light);font-size:12px;line-height:21px;color:var(--muted)}
.what-col b{color:var(--navy);font-style:italic;font-weight:700}
.pillar{position:absolute;left:829px;width:198px;height:40px;border:1px solid #e3e3e8;display:flex;align-items:center;justify-content:space-between;padding-left:9px;font-family:var(--serif);font-style:italic;font-size:15px;color:var(--navy);background:#fff}
.pillar .ico{width:44px;height:38px;border-left:1px solid #e3e3e8;display:flex;align-items:center;justify-content:center}

/* who we are */
.who-text{position:absolute;left:178px;top:975px;width:420px;font-family:var(--light);font-size:11.5px;line-height:18px;color:#333}
.who-text p{margin-bottom:18px}
.who-photo{position:absolute;left:614px;top:840px;width:586px;height:384px;background:linear-gradient(120deg,#cfd6e4 0%,#6b7fb3 40%,#2b44b8 70%,#0e1d7a 100%)}

/* services */
.services{position:absolute;left:0;top:1224px;width:1200px;height:506px;background:var(--teal)}
.service-card{position:absolute;top:112px;width:277px;height:279px;background:#fff}
.service-card .thumb{height:197px;background:linear-gradient(135deg,#6a5a4c,#a9a49c 45%,#d8d8d4 60%,#4d4640)}
.service-card .label{position:absolute;left:29px;top:235px;font-size:15px;font-weight:600;color:var(--navy)}
.service-card .more{position:absolute;right:30px;top:228px;width:32px;height:32px;border-radius:50%;border:1px solid #d4d4d4;display:flex;align-items:center;justify-content:center}
.see-all{position:absolute;left:545px;top:433px;width:112px;height:31px;border:1.5px solid var(--navy);border-radius:3px;font-size:13px;color:var(--navy);display:flex;align-items:center;justify-content:center}

/* expertise */
.sme-photo{position:absolute;left:710px;top:1749px;width:317px;height:514px;background:linear-gradient(160deg,#e8e6e2 0%,#b89a86 35%,#7d6456 60%,#3a3f55 100%)}
.sme-card{position:absolute;width:299px;height:163px;background:#fff;box-shadow:0 6px 20px rgba(0,0,0,.08);padding:25px 20px 0 76px}
.sme-card.dark{background:var(--navy)}
.sme-card h3{font-size:16px;font-weight:600;color:var(--navy);margin-bottom:9px}
.sme-card p{font-family:var(--light);font-size:11.5px;line-height:22px;color:var(--navy)}
.sme-card.dark h3,.sme-card.dark p{color:#fff}
.sme-card .ico{position:absolute;left:25px;top:29px}

/* consultation form */
.consult{position:absolute;left:0;top:2313px;width:1200px;height:312px;background:var(--navy)}
.field-label{position:absolute;font-size:12px;font-weight:600;color:#fff}
.field{position:absolute;height:40px;background:#fff;font-family:var(--light);font-size:11px;color:#9a9a9a;display:flex;align-items:center;padding-left:15px}
.field.center{justify-content:center;padding-left:0}
.consult-btn{position:absolute;left:469px;top:233px;width:262px;height:40px;background:var(--teal);color:var(--navy);font-family:var(--light);font-size:14px;display:flex;align-items:center;justify-content:center;gap:6px}

/* testimonials */
.testimonials{position:absolute;left:0;top:2625px;width:1200px;height:421px;background:var(--teal)}
.quote{position:absolute;width:400px}
.quote .text{margin-top:20px;font-family:var(--light);font-size:12px;line-height:23px;color:var(--navy)}
.client{position:absolute;display:flex;align-items:center;gap:14px}
.client .avatar{width:38px;height:38px;border-radius:50%;background:#fff}
.client strong{display:block;font-family:var(--light);font-weight:400;font-size:13px;color:var(--navy)}
.client span{font-family:var(--light);font-size:12px;color:var(--navy)}
.slider-nav{position:absolute;left:565px;top:367px;display:flex;gap:1px}
.slider-nav span{width:35px;height:54px;background:var(--navy);display:flex;align-items:center;justify-content:center}

/* footer */
.site-footer{position:absolute;left:0;top:3046px;width:1200px;height:378px;background:var(--footer)}
.footer-brand{position:absolute;left:174px;top:60px}
.footer-brand .brand-name{color:#8a8a8a;font-size:20px}
.footer-text{position:absolute;top:132px;width:204px;font-family:var(--light);font-size:9.5px;line-height:17.5px;color:var(--footer-text)}
.footer-head{position:absolute;top:56px;font-size:13.5px;font-weight:700;color:#fff}
.footer-head::after{content:"";display:block;width:43px;height:3px;background:var(--teal);margin-top:9px}
.footer-links{position:absolute;left:642px;top:118px;list-style:none;font-family:var(--light);font-size:10px;color:var(--footer-text)}
.footer-links li{height:25.5px;display:flex;align-items:center;gap:10px}
.footer-links li::before{content:"›";color:var(--teal);font-size:14px}
.contact{position:absolute;left:829px;top:118px;width:200px;font-family:var(--light);font-size:9.5px;color:var(--footer-text)}
.contact div{display:flex;gap:10px;line-height:26px}
.contact svg{flex:none;margin-top:8px}
.copyright{position:absolute;left:0;top:334px;width:1200px;text-align:center;font-family:var(--light);font-size:9.5px;color:var(--footer-text)}
.copyright em{font-style:normal;color:var(--teal)}
</style>
</head>
<body>

<header class="site-header">
  <div class="brand">
    <span class="brand-name">Calder Bid Partners</span>
    <span class="brand-dot"></span>
  </div>
  <div class="social" aria-label="Social links"><span></span><span></span><span></span><span></span><span></span><span></span></div>
  <nav class="main-nav">
    <a class="active">Home</a><a>Work with Us</a><a>Work for Us</a><a>About Us</a><a>Contact</a>
  </nav>
</header>

<section class="hero">
  <div class="hero-photo" role="img" aria-label="Photo of an engineer in a plaid shirt soldering a circuit board"></div>
  <div class="hero-disc"></div>
  <h1 class="hero-title">Generate<br>Success</h1>
  <p class="hero-sub">Fuel Innovation in Proposal<br>Excellence with Calder Bid Partners!</p>
  <a class="hero-btn">Click here to explore our services
    <svg width="10" height="8" viewBox="0 0 10 8"><path d="M0 4h8M5 1l3 3-3 3" stroke="#120d62" stroke-width="1.4" fill="none"/></svg></a>
  <div class="hero-dots"><span class="on"></span><span></span><span></span></div>
</section>
<div class="hero-shadow"></div>

<h2 class="section-title" style="left:175px;top:508px">What We Do</h2>
<div class="what-col" style="left:179px;top:568px">Calder Bid Partners, specializes in advancing an organization through a comprehensive suite of services designed to modernize the proposal development process. From innovative Capture Management strategies that pinpoint lucrative opportunities, meticulous Proposal Development services that transform concepts into effective narratives, and cutting-edge Generative AI techniques that create domain-aware content accelerating proposal draft development, we are your dedicated partner in securing success. With a unique fusion of technical</div>
<div class="what-col" style="left:537px;top:566px;width:280px">and exceptional writing capabilities, we surpass industry standards and set new benchmarks for excellence.<br><br>Discover a dynamic approach to proposal consulting that goes beyond conventional boundaries—choose Calder Bid Partners for solutions that <b>Enhance</b> the quality of your work, <b>Elevate</b> your corporate advantage, and <b>Expand</b> your industry presence.</div>

<div class="pillar" style="top:572px">Capture Management:<span class="ico"><svg width="32" height="30" viewBox="0 0 32 30"><circle cx="16" cy="9" r="7" fill="#120d62"/><path d="M2 30c0-9 6-13 14-13s14 4 14 13z" fill="#120d62"/></svg></span></div>
<div class="pillar" style="top:632px">Proposal Development:<span class="ico"><svg width="32" height="30" viewBox="0 0 32 30"><circle cx="16" cy="9" r="7" fill="#120d62"/><path d="M2 30c0-9 6-13 14-13s14 4 14 13z" fill="#120d62"/></svg></span></div>
<div class="pillar" style="top:692px">Generative AI:<span class="ico"><svg width="32" height="30" viewBox="0 0 32 30"><circle cx="16" cy="9" r="7" fill="#120d62"/><path d="M2 30c0-9 6-13 14-13s14 4 14 13z" fill="#120d62"/></svg></span></div>

<h2 class="section-title" style="left:178px;top:898px">Who We Are</h2>
<div class="who-text">
  <p>Lorem Ipsum is simply dummy text of the printing and typesetting industry. Lorem Ipsum has been the industry's standard dummy text ever since the 1500s, when an unknown printer took a galley of type and scrambled it to make a type specimen book. It has survived not only five centuries, but also the leap into electronic typesetting, remaining essentially unchanged. It was popularised in the 1960s with the release of Dryline sheets containing Lorem Ipsum passages, and more recently with desktop publishing software like PageSetter including versions of Lorem Ipsum.</p>
  <p>Lorem Ipsum is simply dummy text of the printing and typesetting industry. Lorem Ipsum has been the industry's standard dummy text ever since the</p>
</div>
<div class="who-photo" role="img" aria-label="Photo of a professional typing on a laptop with a blue digital network overlay"></div>

<section class="services">
  <h2 class="section-title" style="left:0;width:1200px;text-align:center;top:38px">Our Services</h2>
  <div class="service-card" style="left:173px"><div class="thumb" role="img" aria-label="Photo of a humanoid robot sitting on a sofa in a living room"></div><span class="label">Generative AI</span><span class="more"><svg width="6" height="9" viewBox="0 0 6 9"><path d="M1 1l3.5 3.5L1 8" stroke="#333" fill="none"/></svg></span></div>
  <div class="service-card" style="left:473px"><div class="thumb" role="img" aria-label="Photo of a humanoid robot sitting on a sofa in a living room"></div><span class="label">Generative AI</span><span class="more"><svg width="6" height="9" viewBox="0 0 6 9"><path d="M1 1l3.5 3.5L1 8" stroke="#333" fill="none"/></svg></span></div>
  <div class="service-card" style="left:772px"><div class="thumb" role="img" aria-label="Photo of a humanoid robot sitting on a sofa in a living room"></div><span class="label">Generative AI</span><span class="more"><svg width="6" height="9" viewBox="0 0 6 9"><path d="M1 1l3.5 3.5L1 8" stroke="#333" fill="none"/></svg></span></div>
  <a class="see-all">See all services</a>
</section>

<h2 class="section-title" style="left:171px;top:1804px">Subject Matter Expertise</h2>
<div class="sme-photo" role="img" aria-label="Photo of a team of colleagues working together at a computer"></div>
<div class="sme-card dark" style="left:177px;top:1887px">
  <svg class="ico" width="34" height="34" viewBox="0 0 34 34"><circle cx="17" cy="17" r="10" fill="none" stroke="#1ff0b8" stroke-width="1.6"/><text x="17" y="21" font-size="9" font-family="Montserrat,sans-serif" text-anchor="middle" fill="#1ff0b8">AI</text><path d="M17 1v5M17 28v5M1 17h5M28 17h5M5 5l4 4M25 25l4 4M29 5l-4 4M9 25l-4 4" stroke="#1ff0b8" stroke-width="1.6"/></svg>
  <h3>Generative AI</h3><p>Lorem Ipsum is simply dummy text of the printing and typesetting industry</p></div>
<div class="sme-card" style="left:477px;top:1887px">
  <svg class="ico" width="34" height="34" viewBox="0 0 34 34"><circle cx="17" cy="17" r="9" fill="none" stroke="#1ff0b8" stroke-width="3"/><circle cx="17" cy="17" r="3" fill="#1ff0b8"/><path d="M17 2v6M17 26v6M2 17h6M26 17h6M6 6l4 4M24 24l4 4M28 6l-4 4M10 24l-4 4" stroke="#1ff0b8" stroke-width="3"/></svg>
  <h3>Hardware Engineering</h3><p>Lorem Ipsum is simply dummy text of the printing and typesetting industry</p></div>
<div class="sme-card" style="left:177px;top:2053px">
  <svg class="ico" width="34" height="34" viewBox="0 0 34 34"><path d="M17 4c-7 0-12 5-12 11 0 6 4 9 6 12h12c2-3 6-6 6-12 0-6-5-11-12-11z" fill="none" stroke="#1ff0b8" stroke-width="1.6"/><path d="M17 4v23M11 12h6M17 18h6M11 22h6" stroke="#1ff0b8" stroke-width="1.4"/></svg>
  <h3>Systems Engineering</h3><p>Lorem Ipsum is simply dummy text of the printing and typesetting industry</p></div>
<div class="sme-card" style="left:477px;top:2053px">
  <svg class="ico" width="38" height="42" viewBox="0 0 38 42"><rect x="3" y="5" width="26" height="33" rx="2" fill="none" stroke="#1ff0b8" stroke-width="1.8"/><rect x="10" y="2" width="12" height="6" rx="1" fill="#fff" stroke="#1ff0b8" stroke-width="1.6"/><path d="M8 16h16M8 22h16M8 28h10" stroke="#1ff0b8" stroke-width="1.6"/><circle cx="29" cy="33" r="7" fill="#1ff0b8"/><path d="M26 33l2 2 4-4" stroke="#fff" stroke-width="1.6" fill="none"/></svg>
  <h3>High-Performance</h3><p>Lorem Ipsum is simply dummy text of the printing and typesetting industry. Lorem Ipsum...</p></div>

<section class="consult">
  <span class="field-label" style="left:177px;top:44px">Your Name*</span>
  <span class="field-label" style="left:614px;top:44px">Your Phone Number</span>
  <div class="field" style="left:173px;top:70px;width:420px">Enter your full name</div>
  <div class="field" style="left:613px;top:70px;width:416px">000 000 0000</div>
  <span class="field-label" style="left:0;width:1200px;text-align:center;top:137px">I would like to discuss*</span>
  <div class="field center" style="left:392px;top:163px;width:415px">sample@email.com</div>
  <a class="consult-btn">Get Free Consultation <svg width="18" height="8" viewBox="0 0 18 8"><path d="M0 4h16M13 1l3 3-3 3" stroke="#120d62" stroke-width="1.4" fill="none"/></svg></a>
</section>

<section class="testimonials">
  <h2 class="section-title" style="left:0;width:1200px;text-align:center;top:42px">Client Testimonials</h2>
  <div class="quote" style="left:174px;top:100px">
    <svg width="22" height="17" viewBox="0 0 22 17"><path d="M0 17V9C0 3 3 1 8 0v3C5 4 4 6 4 8h5v9zM13 17V9c0-6 3-8 8-9v3c-3 1-4 3-4 5h5v9z" fill="#120d62"/></svg>
    <p class="text">Lorem Ipsum is simply dummy text of the printing and typesetting industry. Lorem Ipsum has been the industry's standard dummy text ever since the 1500s, when an unknown printer took a galley of type and scrambled it to make a type specimen book. It has survived not</p>
  </div>
  <div class="quote" style="left:625px;top:100px">
    <svg width="22" height="17" viewBox="0 0 22 17"><path d="M0 17V9C0 3 3 1 8 0v3C5 4 4 6 4 8h5v9zM13 17V9c0-6 3-8 8-9v3c-3 1-4 3-4 5h5v9z" fill="#120d62"/></svg>
    <p class="text">Lorem Ipsum is simply dummy text of the printing and typesetting industry. Lorem Ipsum has been the industry's standard dummy text ever since the 1500s, when an unknown printer took a galley of type and scrambled it to make a type specimen book. It has survived not only five centuries, but also the leap into electronic typesetting,</p>
  </div>
  <div class="client" style="left:174px;top:285px"><span class="avatar"></span><div><strong>CLIENT NAME</strong><span>Designation</span></div></div>
  <div class="client" style="left:625px;top:285px"><span class="avatar"></span><div><strong>CLIENT NAME</strong><span>Designation</span></div></div>
  <div class="slider-nav">
    <span><svg width="8" height="12" viewBox="0 0 8 12"><path d="M6 1L1 6l5 5" stroke="#fff" stroke-width="1.5" fill="none"/></svg></span>
    <span><svg width="8" height="12" viewBox="0 0 8 12"><path d="M2 1l5 5-5 5" stroke="#fff" stroke-width="1.5" fill="none"/></svg></span>
  </div>
</section>

<footer class="site-footer">
  <div class="footer-brand"><span class="brand-name">Calder Bid Partners</span></div>
  <p class="footer-text" style="left:174px">Lorem Ipsum is simply dummy text of the printing and typesetting industry. Lorem Ipsum has been the industry's standard dummy text ever since the 1500s, when an unknown printer took a galley.</p>
  <p class="footer-text" style="left:392px">Lorem Ipsum is simply dummy text of the printing and typesetting industry. Lorem Ipsum has been the industry's standard dummy text ever since the 1500s, when an unknown printer took a galley.</p>
  <div class="footer-head" style="left:642px">Explore Our Site</div>
  <ul class="footer-links"><li>Home</li><li>Work with Us</li><li>Work for Us</li><li>About Us</li><li>Contact</li></ul>
  <div class="footer-head" style="left:829px">Keep In Touch</div>
  <div class="contact">
    <div><svg width="9" height="11" viewBox="0 0 9 11"><path d="M4.5 11S0 6.5 0 4.5a4.5 4.5 0 019 0C9 6.5 4.5 11 4.5 11z" fill="#1ff0b8"/><circle cx="4.5" cy="4.5" r="1.6" fill="#333"/></svg><span>Lorem Ipsum is simply dummy text of the printing and typesetting industry</span></div>
    <div><svg width="10" height="10" viewBox="0 0 10 10"><path d="M2 0l2 2.5-1.2 1.3c.8 1.5 2 2.6 3.4 3.4L7.5 6 10 8l-1.5 2C4 9.5.5 6 0 1.5z" fill="#1ff0b8"/></svg><span>000 000 000 / 000 000 000</span></div>
    <div><svg width="11" height="8" viewBox="0 0 11 8"><rect width="11" height="8" fill="#1ff0b8"/><path d="M0 0l5.5 4.5L11 0" stroke="#333" fill="none"/></svg><span>sales@email.com</span></div>
  </div>
  <p class="copyright">© Copyrights 2024 <em>Calder Bid Partners</em>. All rights reserved.</p>
</footer>

</body>
</html>
```